Re-Design Business Card and Logo for Plastic Printing

Business is a small financial planning (investments, insurance, retirement, etc.) firm. The majority of our clients are 55+ years old, professional occupations (pilots, doctors, bankers, etc.) but not necessarily "high net worth."
I would like to have a design that would be used on clear plastic business cards. I have found a vendor that makes these but I do not have the ability to design these like I want.
I do have one proof but I just don't feel like it's the right one for me. Also, I feel that I need some help with a logo redesign so maybe someone could handle that for me as well.
I want the final design to "eye catching" but still be tasteful. I am open to suggestion regarding colors and such.
I will include the old design as well as the new proof I have to give you an idea of what I current have. Keep in mind, I have no allegiance to the attached designs.
For the second file (Business Card New Proof), the white space shown will be transparent when printed on plastic card.
Target Market(s)
Mostly people age 55+ in professional occupations.
Industry/Entity Type
Financial Service
Contact Information for Business Card
Looking for design that can be printed on clear plastic cards (if possible).
Logo Text
HWC - Harborline Wealth Counsel
Requirements
Must have
- Must be double sided because disclosure is required for compliance reasons.
Designations (must include the Registered trademark symbol as follows)...
MBA, ChFC®, CLU®, CRPS®
Nice to have
- The little icons next to email, phone and fax are nice.
Should not have
- I think I would like to eliminate the Owner and Co-Founder line that you see on the attachments.

```html
<!DOCTYPE html>
<html lang="en">
<head>
<meta charset="utf-8">
<title>Harborline Wealth Counsel – Business Card</title>
<link href="https://fonts.googleapis.com/css2?family=Tinos:wght@400;700&display=swap" rel="stylesheet">
<style>
  :root{
    --stage:#2b2b2e;
    --navy:#2e3a7e;
    --frost:#aeb1b6;
    --frost-edge:#e4e5e7;
    --white:#ffffff;
    --ink-soft:#5f6268;
    --serif:"Tinos","Times New Roman",serif;
  }
  *{margin:0;padding:0;box-sizing:border-box}
  html,body{width:1200px;height:800px;overflow:hidden}
  body{background:var(--stage);font-family:var(--serif);display:flex;flex-direction:column;align-items:center;justify-content:center;gap:36px}
  .card{position:relative;width:620px;height:354px;border-radius:16px;overflow:hidden}
  .card-shape{position:absolute;inset:0;width:100%;height:100%}
  .brand{position:absolute;text-align:left}
  .brand-name{font-weight:400;line-height:1;letter-spacing:2px}
  .brand-tag{font-size:11px;margin-top:4px;letter-spacing:.3px}

  /* front */
  .card-front .brand{left:34px;top:120px}
  .card-front .brand-name{font-size:66px;color:var(--navy)}
  .card-front .brand-tag{color:var(--ink-soft)}
  .holder{position:absolute;right:34px;top:28px;color:var(--white);text-align:right;white-space:nowrap}
  .holder-name{display:block;font-size:28px;font-weight:700;line-height:1.15}
  .holder-titles{display:block;font-size:14px;font-weight:400;line-height:1.4}
  .address{position:absolute;right:34px;top:112px;color:var(--white);font-size:22px;line-height:1.25;text-align:right;font-style:normal}
  .contacts{position:absolute;right:30px;bottom:26px;color:var(--white);font-size:15px;list-style:none;text-align:right}
  .contacts li{display:flex;align-items:center;justify-content:flex-end;gap:10px;line-height:1.65}
  .contacts svg{width:16px;height:16px;fill:var(--white)}

  /* back */
  .card-back .brand{right:44px;top:70px;text-align:right}
  .card-back .brand-name{font-size:78px;color:var(--white)}
  .card-back .brand-tag{color:var(--white)}
  .disclosure{position:absolute;right:40px;top:210px;width:300px;color:var(--white);font-size:11px;line-height:1.45;text-align:center}
</style>
</head>
<body>

<section class="card card-front">
  <svg class="card-shape" viewBox="0 0 620 354" preserveAspectRatio="none" aria-hidden="true">
    <rect width="620" height="354" fill="var(--navy)"/>
    <path d="M0 0 H258 C320 110 284 262 150 354 H0 Z" fill="var(--frost)"/>
    <path d="M258 0 C320 110 284 262 150 354" fill="none" stroke="var(--frost-edge)" stroke-width="7"/>
  </svg>
  <div class="brand">
    <div class="brand-name">HWC</div>
    <div class="brand-tag">Harborline Wealth Counsel</div>
  </div>
  <div class="holder">
    <span class="holder-name">Owen Kessler</span>
    <span class="holder-titles">MBA, ChFC®, CLU®, CRPS®</span>
  </div>
  <address class="address">
    270 Lantern Bay Dr.<br>Suite B140<br>Norfield, VA 23519
  </address>
  <ul class="contacts">
    <li>555 218 3904
      <svg viewBox="0 0 16 16"><path d="M3 1h3l1.5 4-2 1.3a9 9 0 0 0 4.2 4.2L11 8.5l4 1.5v3a2 2 0 0 1-2 2A12 12 0 0 1 1 3a2 2 0 0 1 2-2z"/></svg></li>
    <li>okessler@harborlinewc.com
      <svg viewBox="0 0 16 16"><path d="M1 3h14v10H1z M2 4l6 5 6-5" fill="none" stroke="#fff" stroke-width="1.5"/></svg></li>
    <li>Toll Free 800 555 0147
      <svg viewBox="0 0 16 16"><path d="M4 1h8v4H4z M1 6h14v6h-3v3H4v-3H1z M5 10v4h6v-4z"/></svg></li>
  </ul>
</section>

<section class="card card-back">
  <svg class="card-shape" viewBox="0 0 620 354" preserveAspectRatio="none" aria-hidden="true">
    <rect width="620" height="354" fill="var(--navy)"/>
    <path d="M0 0 H236 C300 90 280 190 150 262 C100 290 40 300 0 304 Z" fill="var(--frost)"/>
    <path d="M236 0 C300 90 280 190 150 262 C100 290 40 300 0 304" fill="none" stroke="var(--frost-edge)" stroke-width="7"/>
  </svg>
  <div class="brand">
    <div class="brand-name">HWC</div>
    <div class="brand-tag">Harborline Wealth Counsel</div>
  </div>
  <p class="disclosure">Owen Kessler is a registered representative of and offers securities through Example Securities, Member Northgate Exchange. Advisory services offered through Sample Advisors, a registered investment adviser. Harborline Wealth Counsel is not affiliated with either firm.</p>
</section>

</body>
</html>
```